Talvo shoes is a wholesale shoe sales company , mostly working in female shoes and kiddies shoes with a small mens section . looking for a clean slick look. http://www.kemrafootwear.co.za/shop/ is a good reference

It Company

```html
<!DOCTYPE html>
<html lang="en">
<head>
<meta charset="utf-8">
<title>Talvo Shoes</title>
<link rel="stylesheet" href="https://fonts.googleapis.com/css2?family=Raleway:wght@300;400;500;800&family=Arimo:wght@400;700&display=swap">
<style>
:root{
  --red:#b81c22;
  --ink:#222222;
  --text:#333333;
  --muted:#666666;
  --line:#e2e2e2;
  --hero:#f4f4f4;
  --dark:#333333;
  --footer:#323232;
  --white:#ffffff;
}
*{box-sizing:border-box;margin:0;padding:0}
html,body{width:1200px;height:1072px;overflow:hidden;background:var(--white)}
body{position:relative;font-family:Arimo,Arial,sans-serif;color:var(--text)}
.abs{position:absolute}

/* header */
.phone{left:107px;top:32px;display:flex;align-items:center;gap:2px;font-family:Raleway,sans-serif;font-weight:400;font-size:21px;color:var(--ink)}
.email{left:107px;top:66px;font-family:Raleway,sans-serif;font-size:14px;color:var(--red)}
.brand{left:0;width:1200px;top:20px;text-align:center;font-family:Raleway,sans-serif;font-weight:400;font-size:56px;color:var(--ink);letter-spacing:0}
.account{right:107px;top:38px;font-size:12px;color:var(--muted)}
.account .sep{color:var(--red);margin:0 7px}
.account .welcome{color:var(--red)}
.search{left:898px;top:66px;width:197px;height:24px;border:1px solid var(--line);background:var(--white)}
.search-btn{position:absolute;right:-1px;top:-1px;width:27px;height:24px;background:var(--dark);display:flex;align-items:center;justify-content:center}

/* nav */
.nav{left:117px;top:111px;display:flex;font-size:15px;color:var(--ink);text-transform:uppercase}
.nav a{color:inherit;text-decoration:none;height:27px;line-height:27px;padding:0 11px;margin-right:19px}
.nav a.active{background:var(--red);color:var(--white);border-radius:7px}

/* hero */
.hero{left:0;top:148px;width:1200px;height:389px;background:var(--hero)}
.hero-backdrop{left:140px;top:40px;width:420px;height:330px;background:radial-gradient(ellipse at center,#f2dfe5 0%,#f4eaed 45%,rgba(244,244,244,0) 75%)}
.hero-photo{left:615px;top:0;width:485px;height:385px;background:linear-gradient(160deg,#f4f4f4 0%,#e9d6c9 40%,#2a2a2a 75%,#f0f0f0 100%)}
.hero-title{left:101px;top:128px;font-family:Raleway,sans-serif;font-weight:800;font-size:51px;letter-spacing:2px;color:var(--ink)}
.hero-title .accent{color:var(--red)}
.hero-copy{left:104px;top:189px;width:430px;font-family:Raleway,sans-serif;font-size:15px;line-height:20px;color:var(--ink)}

/* best sellers */
.rule{left:101px;top:592px;width:998px;height:1px;background:var(--line)}
.section-title{left:500px;top:567px;width:198px;height:50px;background:var(--white);border:1px solid var(--line);text-align:center;line-height:46px;font-family:Raleway,sans-serif;font-weight:500;font-size:29px;color:var(--ink)}
.arrow{top:753px}
.card{top:653px;width:217px;height:255px;border:1px solid var(--line);background:var(--white)}
.card-photo{position:absolute;left:8px;top:8px;width:199px;height:170px}
.card-name{position:absolute;left:11px;top:186px;font-family:Raleway,sans-serif;font-size:15px;color:var(--ink);white-space:nowrap}
.card-name span{color:#555}
.price{position:absolute;left:10px;top:215px;width:69px;height:32px;background:var(--dark);color:var(--white);font-size:14px;line-height:32px;padding-left:4px}
.cart{position:absolute;left:88px;top:215px;width:118px;height:32px;background:var(--red);color:var(--white);font-size:14px;line-height:32px;display:flex;align-items:center}
.cart svg{margin:0 14px 0 6px}
.sale{left:103px;top:648px}

/* footer */
.footer{left:0;top:948px;width:1200px;height:124px;background:var(--footer);color:var(--white)}
.footer-links{position:absolute;left:102px;top:29px;font-family:Raleway,sans-serif;font-size:13px;text-transform:uppercase;white-space:nowrap}
.footer-links .bar{margin:0 12px}
.copyright{position:absolute;left:101px;top:73px;font-size:12px}
.newsletter-label{position:absolute;left:892px;top:18px;font-family:Raleway,sans-serif;font-size:16px}
.newsletter-input{position:absolute;left:892px;top:48px;width:208px;height:26px;background:var(--white)}
.newsletter-input svg{position:absolute;right:4px;top:6px}
.follow{position:absolute;left:892px;top:90px;font-family:Raleway,sans-serif;font-size:16px}
.social{position:absolute;left:1002px;top:90px;display:flex;gap:11px}
.social span{width:18px;height:18px;border-radius:50%;background:#6a6a6a}
</style>
</head>
<body>

<header>
  <div class="abs phone">
    <svg width="22" height="26" viewBox="0 0 22 26" aria-hidden="true"><path d="M5 1 L9 6 L6.5 9 C8 13 10 16 13 18 L16 15.5 L21 20 L18 24 C10 23 2 13 1 5 Z" fill="var(--ink)"/></svg>
    <span>+9815-555-317</span>
  </div>
  <div class="abs email">Suport@talvoshoes.com</div>
  <div class="abs brand">Talvo Shoes</div>
  <div class="abs account">Your Account<span class="sep">|</span><span class="welcome">Welcome,</span> ( Log in )</div>
  <div class="abs search">
    <div class="search-btn">
      <svg width="16" height="16" viewBox="0 0 16 16" aria-hidden="true"><circle cx="6.5" cy="6.5" r="5" fill="none" stroke="#fff" stroke-width="1.8"/><line x1="10" y1="10" x2="15" y2="15" stroke="#fff" stroke-width="2"/></svg>
    </div>
  </div>
  <nav class="abs nav">
    <a class="active">Ladies</a><a>Mens</a><a>Girls</a><a>Boys</a><a>Accessories</a><a>Events</a><a>About Us</a><a>Stores</a><a>FAQ</a><a>Contact</a>
  </nav>
</header>

<section class="abs hero">
  <div class="abs hero-backdrop" role="img" aria-label="Faint pink strappy heels in the background"></div>
  <div class="abs hero-photo" role="img" aria-label="Photo of feet wearing black jewelled high-heel sandals"></div>
  <h1 class="abs hero-title"><span class="accent">STYLE</span> TO FUN</h1>
  <p class="abs hero-copy">Lorem ipsum dolor sit amet, consectetur adipisicing elit, sed do eiusmod tempor incididunt ut labore et dolore magna aliqua. Ut enim ad minim</p>
</section>

<section>
  <div class="abs rule"></div>
  <h2 class="abs section-title">Best Sallers</h2>

  <svg class="abs arrow" style="left:68px" width="24" height="28" viewBox="0 0 24 28" aria-hidden="true"><path d="M18 1 L5 14 L18 27" fill="none" stroke="var(--ink)" stroke-width="5"/></svg>
  <svg class="abs arrow" style="left:1105px" width="24" height="28" viewBox="0 0 24 28" aria-hidden="true"><path d="M6 1 L19 14 L6 27" fill="none" stroke="var(--ink)" stroke-width="5"/></svg>

  <article class="abs card" style="left:108px">
    <div class="card-photo" role="img" aria-label="Pink ruffled high-heel sandals" style="background:linear-gradient(135deg,#fff 0%,#f6c2dc 40%,#e0388f 65%,#fff 100%)"></div>
    <p class="card-name">Lorem ipsum dolor <span>sit amet,</span></p>
    <div class="price">$ 250.00</div>
    <div class="cart"><svg width="22" height="20" viewBox="0 0 22 20" aria-hidden="true"><path d="M1 2 H5 L8 13 H18 L20 5 H6" fill="none" stroke="#fff" stroke-width="2"/><circle cx="9" cy="17" r="2" fill="#fff"/><circle cx="17" cy="17" r="2" fill="#fff"/></svg>Add To Cart</div>
  </article>

  <article class="abs card" style="left:360px">
    <div class="card-photo" role="img" aria-label="Turquoise beaded flat sandal with floral print" style="background:linear-gradient(160deg,#fff 0%,#bfe4e6 40%,#c7a6b8 70%,#fff 100%)"></div>
    <p class="card-name">Lorem ipsum dolor <span>sit amet,</span></p>
    <div class="price">$ 250.00</div>
    <div class="cart"><svg width="22" height="20" viewBox="0 0 22 20" aria-hidden="true"><path d="M1 2 H5 L8 13 H18 L20 5 H6" fill="none" stroke="#fff" stroke-width="2"/><circle cx="9" cy="17" r="2" fill="#fff"/><circle cx="17" cy="17" r="2" fill="#fff"/></svg>Add To Cart</div>
  </article>

  <article class="abs card" style="left:617px">
    <div class="card-photo" role="img" aria-label="Blue glitter ballet flats with bows" style="background:linear-gradient(160deg,#fff 0%,#8fb4c4 45%,#4d7f99 65%,#fff 100%)"></div>
    <p class="card-name">Lorem ipsum dolor <span>sit amet,</span></p>
    <div class="price">$ 250.00</div>
    <div class="cart"><svg width="22" height="20" viewBox="0 0 22 20" aria-hidden="true"><path d="M1 2 H5 L8 13 H18 L20 5 H6" fill="none" stroke="#fff" stroke-width="2"/><circle cx="9" cy="17" r="2" fill="#fff"/><circle cx="17" cy="17" r="2" fill="#fff"/></svg>Add To Cart</div>
  </article>

  <article class="abs card" style="left:873px">
    <div class="card-photo" role="img" aria-label="Cream ballet flats with black toe caps" style="background:linear-gradient(160deg,#fff 0%,#efe3de 45%,#2b2b2b 70%,#fff 100%)"></div>
    <p class="card-name">Lorem ipsum dolor <span>sit amet,</span></p>
    <div class="price">$ 250.00</div>
    <div class="cart"><svg width="22" height="20" viewBox="0 0 22 20" aria-hidden="true"><path d="M1 2 H5 L8 13 H18 L20 5 H6" fill="none" stroke="#fff" stroke-width="2"/><circle cx="9" cy="17" r="2" fill="#fff"/><circle cx="17" cy="17" r="2" fill="#fff"/></svg>Add To Cart</div>
  </article>

  <svg class="abs sale" width="126" height="128" viewBox="0 0 126 128" aria-label="Sale">
    <path d="M0 14 Q0 0 14 0 H126 V0 L0 126 Z" fill="none"/>
    <path d="M0 0 H126 L124 6 C60 8 10 50 6 124 L0 128 Z" fill="var(--red)"/>
    <path d="M0 0 H120 L0 100 Z" fill="#d62d42" opacity=".6"/>
    <text x="28" y="48" transform="rotate(-45 28 48)" fill="#fff" font-family="Raleway,sans-serif" font-size="17" font-weight="500" text-anchor="middle">SALE</text>
  </svg>
</section>

<footer class="abs footer">
  <div class="footer-links">Ladies<span class="bar">|</span> Mens<span class="bar">|</span>Girls<span class="bar">|</span>Boys<span class="bar">|</span>Accessories<span class="bar">|</span>Events<span class="bar">|</span>About Us<span class="bar">|</span>Stores<span class="bar">|</span>FAQ<span class="bar">|</span>Contact</div>
  <p class="copyright">Copyright © 2012 Talvo Shoes. All rights reserved.</p>
  <div class="newsletter-label">NEWSLETTER</div>
  <div class="newsletter-input"><svg width="12" height="14" viewBox="0 0 12 14" aria-hidden="true"><path d="M2 1 L9 7 L2 13" fill="none" stroke="var(--red)" stroke-width="2.5"/></svg></div>
  <div class="follow">FOLLOW US</div>
  <div class="social" aria-label="Social links"><span></span><span></span><span></span></div>
</footer>

</body>
</html>
```